Business Card Design Project - The Bridgeway Partners

Company Name - The Bridgeway Partners

We need a unique logo and business cards

We are a team of experienced IT professionals who specialize in providing business value to organizations via the analysis and understanding the challenges of your particular organization. We focus on understanding the challenges first, and execute against your priorities partnering with your highly valued key resources.

Our extensive experience and focus on Agile delivery methodologies help our clients continuously improve and deliver quality solutions. Using this approach we will always deliver the greatest return on your investments.

Target Market(s)

Large organizations IT departments

Industry/Entity Type

Business

Font styles to use
Serif
Sans Serif

Requirements
Should not have
• no pictures

```html
<!DOCTYPE html>
<html lang="en">
<head>
<meta charset="utf-8">
<title>The Bridgeway Partners – Business Cards</title>
<link href="https://fonts.googleapis.com/css2?family=Michroma&family=Oswald:wght@500&family=Roboto+Condensed:wght@400&display=swap" rel="stylesheet">
<style>
  :root {
    --bg: #e9e7e4;
    --paper: #f7f7f7;
    --teal: #1aa7ad;
    --teal-light: #2cb9bf;
    --teal-dark: #14878c;
    --ink-white: #ffffff;
    --shadow: rgba(0,0,0,0.18);
  }
  * { box-sizing: border-box; margin: 0; padding: 0; }
  html, body { width: 1200px; height: 970px; overflow: hidden; background: var(--bg); }
  .canvas { position: relative; width: 1200px; height: 970px; }

  .card {
    position: absolute;
    width: 580px; height: 332px;
    left: 310px;
    background: var(--paper);
    box-shadow: 0 10px 28px var(--shadow);
    overflow: hidden;
  }
  .card--front { top: 96px; }
  .card--back  { top: 540px; }

  .wordmark {
    font-family: "Michroma", sans-serif;
    color: var(--teal);
    letter-spacing: 0.08em;
    text-transform: uppercase;
    white-space: nowrap;
    display: flex; align-items: center; gap: 12px;
  }
  .wordmark__dot {
    display: inline-block; flex: none; border-radius: 50%;
    background: var(--teal);
  }
  .card--front .wordmark {
    position: absolute; left: 96px; top: 152px; font-size: 16px;
  }
  .card--front .wordmark__dot { width: 18px; height: 18px; }

  .back__brand {
    position: absolute; left: 0; top: 0; width: 300px; height: 100%;
    display: flex; flex-direction: column; align-items: center; justify-content: center; gap: 14px;
  }
  .back__brand .wordmark { font-size: 11px; }
  .back__brand .wordmark__dot { width: 34px; height: 34px; }

  .back__panel {
    position: absolute; left: 300px; top: 0; width: 280px; height: 100%;
    background: var(--teal);
    color: var(--ink-white);
    font-family: "Roboto Condensed", sans-serif;
  }
  .back__address {
    position: absolute; right: 0; top: 0; width: 100%; height: 86px;
    background: var(--teal-light);
    padding: 20px 22px 0 0;
    text-align: right; font-size: 13px; line-height: 1.45;
  }
  .back__identity {
    position: absolute; right: 0; top: 86px; width: 100%; height: 70px;
    background: var(--teal-dark);
    padding: 12px 22px 0 0; text-align: right;
  }
  .back__name {
    font-family: "Oswald", sans-serif; font-size: 22px; letter-spacing: 0.03em;
    text-transform: uppercase; line-height: 1.1;
  }
  .back__title { font-size: 12px; letter-spacing: 0.12em; text-transform: uppercase; margin-top: 3px; }

  .contact-list {
    position: absolute; right: 22px; top: 178px; list-style: none;
    font-size: 12px; text-align: right;
  }
  .contact-list li {
    display: flex; align-items: center; justify-content: flex-end; gap: 10px;
    height: 24px;
  }
  .contact-list svg { width: 13px; height: 13px; fill: none; stroke: var(--ink-white); stroke-width: 1.6; }
</style>
</head>
<body>
<div class="canvas">

  <section class="card card--front" aria-label="Business card front">
    <div class="wordmark"><span class="wordmark__dot"></span>The Bridgeway Partners</div>
  </section>

  <section class="card card--back" aria-label="Business card back">
    <div class="back__brand">
      <span class="wordmark__dot"></span>
      <div class="wordmark">The Bridgeway Partners</div>
    </div>

    <div class="back__panel">
      <div class="back__address">
        42 Harbor Point Road<br>
        5th Floor Street W.
      </div>
      <div class="back__identity">
        <div class="back__name">Daniel Reyes</div>
        <div class="back__title">General Manager</div>
      </div>
      <ul class="contact-list">
        <li>020 418 5523
          <svg viewBox="0 0 16 16"><path d="M3 2h3l1.5 3.5-2 1.3a8 8 0 0 0 3.7 3.7l1.3-2L14 10v3a1 1 0 0 1-1 1A12 12 0 0 1 2 3a1 1 0 0 1 1-1z"/></svg>
        </li>
        <li>020 418 5524
          <svg viewBox="0 0 16 16"><rect x="4" y="1.5" width="8" height="13" rx="1.5"/><path d="M7 12h2"/></svg>
        </li>
        <li>info@bridgewaypartners.com
          <svg viewBox="0 0 16 16"><rect x="1.5" y="3.5" width="13" height="9" rx="1"/><path d="M1.5 4l6.5 5 6.5-5"/></svg>
        </li>
        <li>www.bridgewaypartners.com
          <svg viewBox="0 0 16 16"><circle cx="8" cy="8" r="6.3"/><path d="M1.7 8h12.6M8 1.7c2 2 2 10.6 0 12.6M8 1.7c-2 2-2 10.6 0 12.6"/></svg>
        </li>
      </ul>
    </div>
  </section>

</div>
</body>
</html>
```